Corvane Supplies Business Card

Professional business card that stand out to our potential customers. Front and back with clean modern design

Industry/Entity Type

Oil and gas

Contact Information for Business Card

Name, address, website , office phone and cell number

Requirements
Must have
• Editable files for each employee

```html
<!DOCTYPE html>
<html lang="en">
<head>
<meta charset="UTF-8">
<title>Corvane Supplies Business Card</title>
<link href="https://fonts.googleapis.com/css2?family=Roboto:wght@400;500;700;900&display=swap" rel="stylesheet">
<style>
  :root {
    --bg: #d4d5d7;
    --card-dark: #1a1a1a;
    --card-light: #ffffff;
    --red: #e91e23;
    --blue: #00aed3;
    --ink: #1c1c1c;
  }
  * { margin: 0; padding: 0; box-sizing: border-box; }
  html, body { width: 900px; height: 1200px; overflow: hidden; }
  body {
    background: var(--bg);
    font-family: "Roboto", Arial, sans-serif;
    position: relative;
    color: var(--ink);
  }
  .card {
    position: absolute;
    left: 134px;
    width: 632px;
    height: 364px;
    overflow: hidden;
  }
  .card--front { top: 210px; background: var(--card-dark); }
  .card--back { top: 624px; background: var(--card-light); }

  .wordmark {
    position: absolute;
    display: flex;
    align-items: center;
    gap: 10px;
    color: var(--red);
    font-weight: 900;
    text-transform: uppercase;
    white-space: nowrap;
    letter-spacing: 0.5px;
  }
  .wordmark__square { background: var(--red); flex: none; }
  .card--front .wordmark {
    left: 50%; top: 50%;
    transform: translate(-50%, -50%);
    font-size: 34px;
  }
  .card--front .wordmark__square { width: 28px; height: 28px; }
  .card--back .wordmark {
    left: 170px; top: 200px;
    transform: translate(-50%, -50%);
    font-size: 22px;
  }
  .card--back .wordmark__square { width: 18px; height: 18px; }

  .divider {
    position: absolute;
    left: 316px;
    width: 2px;
  }
  .divider--top { top: 99px; height: 38px; background: var(--red); }
  .divider--mid { top: 140px; height: 90px; background: var(--blue); left: 315px; width: 3px; }
  .divider--bottom { top: 233px; height: 36px; background: var(--red); }

  .contact { position: absolute; left: 346px; top: 96px; }
  .contact__name { font-size: 25px; font-weight: 700; line-height: 1.2; }
  .contact__first { color: var(--red); }
  .contact__last { color: var(--blue); }
  .contact__role { font-size: 15px; line-height: 1.2; margin-top: 1px; }
  .contact__address { font-size: 15px; line-height: 20px; margin-top: 7px; }
  .contact__list { list-style: none; margin-top: 6px; }
  .contact__item {
    display: flex; align-items: center; gap: 8px;
    font-size: 15px; height: 25.5px;
  }
  .contact__item--phone { letter-spacing: 2.5px; }
  .contact__icon { width: 15px; height: 15px; flex: none; fill: var(--blue); }

  .footer-band { position: absolute; left: 0; bottom: 0; width: 632px; height: 13px; }
</style>
</head>
<body>
  <section class="card card--front" aria-label="Card front">
    <div class="wordmark"><span class="wordmark__square"></span>Corvane Supplies</div>
  </section>

  <section class="card card--back" aria-label="Card back">
    <div class="wordmark"><span class="wordmark__square"></span>Corvane Supplies</div>

    <span class="divider divider--top"></span>
    <span class="divider divider--mid"></span>
    <span class="divider divider--bottom"></span>

    <div class="contact">
      <h1 class="contact__name"><span class="contact__first">Rohan</span> <span class="contact__last">Mehta</span></h1>
      <p class="contact__role">CEO</p>
      <p class="contact__address">420 W.Ridgeline Suite 5<br>Midland, Tx 79701</p>
      <ul class="contact__list">
        <li class="contact__item contact__item--phone">
          <svg class="contact__icon" viewBox="0 0 24 24" aria-hidden="true"><path d="M6.6 10.8a15.1 15.1 0 0 0 6.6 6.6l2.2-2.2c.3-.3.7-.4 1-.2 1.1.4 2.3.6 3.6.6.6 0 1 .4 1 1V20c0 .6-.4 1-1 1A17 17 0 0 1 3 4c0-.6.4-1 1-1h3.5c.6 0 1 .4 1 1 0 1.3.2 2.5.6 3.6.1.3 0 .7-.2 1z"/></svg>
          (555)014-2398
        </li>
        <li class="contact__item">
          <svg class="contact__icon" viewBox="0 0 24 24" aria-hidden="true"><path d="M2 5h20v14H2z M3.5 6.5 12 13l8.5-6.5" fill="var(--blue)" stroke="#fff" stroke-width="1.4"/></svg>
          sales@corvanesupplies.com
        </li>
        <li class="contact__item">
          <svg class="contact__icon" viewBox="0 0 24 24" aria-hidden="true"><circle cx="12" cy="12" r="9.5" fill="none" stroke="var(--blue)" stroke-width="1.8"/><path d="M2.5 12h19M12 2.5v19M12 2.5c-3 3-3 16 0 19M12 2.5c3 3 3 16 0 19M4.5 7h15M4.5 17h15" fill="none" stroke="var(--blue)" stroke-width="1.4"/></svg>
          www.corvanesupplies.com
        </li>
      </ul>
    </div>

    <svg class="footer-band" viewBox="0 0 632 13" preserveAspectRatio="none" aria-hidden="true">
      <polygon points="0,0 324,0 320,13 0,13" fill="var(--red)"/>
      <polygon points="327,0 632,0 632,13 323,13" fill="var(--blue)"/>
    </svg>
  </section>
</body>
</html>
```